Townhome Multi-Family Property Exterior Sign

Hello. We are looking for a new design for our exterior pylon for for a multi-family housing property in Texas. The design will need to go on a new sign panel to replace the existing (see photo of existing). We are looking to see both modern and contemporary designs. Included the sign should be the name, Loma Brisa Townhomes and the web address www.lomabrisatownhomes.example.

Attached here is a PDF file of the proposed new sign shape. We are open to other shape ideas as well if your design would better suit a more rectangular shape.

Industry/Entity Type

Property

Font styles to use
Serif
Sans Serif

Colors
9bcb3c

Requirements
Must have
• Name of building: Loma Brisa Townhomes
• Website: www.lomabrisatownhomes.example
Nice to have
• Address: 412-590 Halvern Ridge Drive (only if it fits nicely)

```html
<!DOCTYPE html>
<html lang="en">
<head>
<meta charset="utf-8">
<title>Loma Brisa Townhomes – Exterior Sign</title>
<link rel="stylesheet" href="https://fonts.googleapis.com/css2?family=Archivo+Black&family=Roboto:wght@400&family=Roboto+Condensed:wght@400;700&display=swap">
<style>
  :root {
    --backdrop: #efeae2;
    --post-green: #0f6b30;
    --brand-lime: #9bcb3c;
    --lime-light: #c9e690;
    --deep-green: #1f7a35;
    --band-green-top: #2e8c3a;
    --band-green-bottom: #80c244;
    --skyline-grey: #e4e4e4;
    --skyline-grey-dark: #d2d2d2;
    --white: #ffffff;
  }
  html, body {
    margin: 0;
    padding: 0;
    width: 1200px;
    height: 854px;
    overflow: hidden;
    background: var(--backdrop);
  }
  .sign {
    position: relative;
    width: 1200px;
    height: 854px;
  }
  .sign-shapes {
    position: absolute;
    inset: 0;
  }
  .brand-name {
    position: absolute;
    left: 0;
    width: 1200px;
    top: 222px;
    margin: 0;
    text-align: center;
    font-family: "Archivo Black", sans-serif;
    font-size: 104px;
    line-height: 1;
    color: var(--white);
    letter-spacing: 2px;
  }
  .property-name {
    position: absolute;
    left: 136px;
    width: 928px;
    top: 388px;
    margin: 0;
    text-align: center;
    font-family: "Archivo Black", sans-serif;
    font-size: 46px;
    line-height: 1;
    letter-spacing: 3px;
    color: var(--deep-green);
  }
  .property-url {
    position: absolute;
    left: 136px;
    width: 928px;
    top: 452px;
    margin: 0;
    text-align: center;
    font-family: "Roboto Condensed", sans-serif;
    font-size: 40px;
    line-height: 1;
    color: var(--deep-green);
  }
  .property-url .url-domain { font-weight: 700; }
  .property-address {
    position: absolute;
    left: 250px;
    width: 700px;
    top: 556px;
    margin: 0;
    text-align: center;
    font-family: "Roboto", sans-serif;
    font-size: 38px;
    line-height: 1;
    color: var(--white);
  }
</style>
</head>
<body>
<main class="sign">
  <svg class="sign-shapes" width="1200" height="854" viewBox="0 0 1200 854" aria-hidden="false">
    <defs>
      <linearGradient id="crown-fill" x1="0" y1="0" x2="0" y2="1">
        <stop offset="0" stop-color="var(--lime-light)"/>
        <stop offset="0.45" stop-color="var(--brand-lime)"/>
        <stop offset="1" stop-color="var(--brand-lime)"/>
      </linearGradient>
      <linearGradient id="skyline-fill" x1="0" y1="0" x2="0" y2="1">
        <stop offset="0" stop-color="var(--skyline-grey)"/>
        <stop offset="1" stop-color="var(--skyline-grey-dark)"/>
      </linearGradient>
      <linearGradient id="address-band-fill" x1="0" y1="0" x2="0" y2="1">
        <stop offset="0" stop-color="var(--band-green-top)"/>
        <stop offset="1" stop-color="var(--band-green-bottom)"/>
      </linearGradient>
    </defs>

    <!-- posts -->
    <g class="post post-left" fill="var(--post-green)">
      <rect x="90" y="284" width="48" height="388"/>
      <polygon points="80,284 146,284 146,278 113,266 80,278"/>
    </g>
    <g class="post post-right" fill="var(--post-green)">
      <rect x="1064" y="280" width="48" height="392"/>
      <polygon points="1054,280 1120,280 1120,274 1087,262 1054,274"/>
    </g>

    <!-- panel crown -->
    <path class="panel-crown" fill="url(#crown-fill)"
          d="M136,300 C300,292 420,184 600,184 C780,184 900,292 1064,300 L1064,356 L136,356 Z"/>

    <!-- skyline band -->
    <rect class="skyline-band" x="136" y="354" width="928" height="170"
          fill="url(#skyline-fill)" role="img" aria-label="Faint grey city skyline illustration with buildings and trees"/>

    <!-- address band -->
    <rect class="address-band" x="136" y="524" width="928" height="104" fill="url(#address-band-fill)"/>
    <rect class="address-frame" x="250" y="544" width="700" height="66" fill="none" stroke="var(--white)" stroke-width="1.5"/>

    <!-- location pin -->
    <g class="pin-icon">
      <circle cx="600" cy="546" r="15" fill="var(--band-green-top)" stroke="var(--white)" stroke-width="1.5"/>
      <path d="M600,539 a5,5 0 0 1 5,5 c0,4 -5,9 -5,9 c0,0 -5,-5 -5,-9 a5,5 0 0 1 5,-5 z" fill="var(--white)"/>
      <circle cx="600" cy="544" r="1.8" fill="var(--band-green-top)"/>
    </g>
  </svg>

  <p class="brand-name">VIREO</p>
  <h1 class="property-name">LOMA BRISA TOWNHOMES</h1>
  <p class="property-url">www.<span class="url-domain">lomabrisatownhomes</span>.example</p>
  <p class="property-address">412-590 HALVERN RIDGE DRIVE</p>
</main>
</body>
</html>
```